4"x9" Roofing Flyer Design - Tile Roofing!

We are looking to create a 4"x9" double sided flyer in full color that displays pictures of before and after of tile underlayment replacement. This would have words as well.

The theme should match the overall theme of our brochure that we already have designed so they are cohesive.

I have uploaded an example of a similar flyer that we like the overall layout of.

Please read the "Design Wording" PDF I uploaded for the words and overall design layout we are looking for on this brochure.

Please let me know if you'd like more photos or anything like that.

Target Market(s)

Retirees

Industry/Entity Type

Roofing

Font styles to use
Other font styles liked:
• Match existing fonts from our brochure

Requirements
Must have
• Must match style of existing brochure (uploaded), font must match closely as well

```html
<!DOCTYPE html>
<html lang="en">
<head>
<meta charset="UTF-8">
<title>Mesa Ridge Roofing – Tile Underlayment Flyer</title>
<link href="https://fonts.googleapis.com/css2?family=Coustard:wght@900&family=Questrial&family=Open+Sans:wght@400;600;700&display=swap" rel="stylesheet">
<style>
  :root {
    --ink: #231f20;
    --orange: #e8591e;
    --white: #ffffff;
    --text: #2b2b2b;
  }
  * { margin: 0; padding: 0; box-sizing: border-box; }
  html, body { width: 1200px; height: 2611px; overflow: hidden; background: var(--white); }
  .flyer { position: relative; width: 1200px; height: 2611px; background: var(--white); }

  .masthead {
    position: absolute; left: 34px; top: 34px; width: 1128px; height: 378px;
    background: var(--ink); text-align: center; color: var(--white);
  }
  .brand-mark {
    position: absolute; left: 564px; top: 104px; width: 66px; height: 66px;
    margin-left: -33px; background: var(--orange);
  }
  .brand-name {
    position: absolute; left: 0; right: 0; top: 216px;
    font-family: "Coustard", Georgia, serif; font-weight: 900;
    font-size: 50px; line-height: 1; color: var(--white);
  }
  .tagline {
    position: absolute; left: 0; right: 0; top: 300px;
    font-family: "Questrial", Arial, sans-serif; font-size: 42px;
    letter-spacing: 2px; line-height: 1; color: var(--orange);
  }
  .phone-bar {
    position: absolute; left: 34px; top: 416px; width: 1128px; height: 86px;
    background: var(--ink); color: var(--white); text-align: center;
    font-family: "Questrial", Arial, sans-serif; font-size: 78px;
    line-height: 86px; letter-spacing: 5px; font-weight: 400;
    -webkit-text-stroke: 1.5px var(--white);
  }

  .photo-grid {
    position: absolute; left: 34px; top: 510px; width: 1128px; height: 840px;
  }
  .photo { position: absolute; width: 562px; height: 414px; overflow: hidden; }
  .photo--tl { left: 0; top: 0; background: linear-gradient(135deg, #7d7a74, #625e58); }
  .photo--tr { left: 570px; top: 0; width: 558px; background: linear-gradient(135deg, #7a7168, #635a52); }
  .photo--bl { left: 0; top: 422px; height: 418px; background: linear-gradient(135deg, #7e8a98, #5e646d); }
  .photo--br { left: 570px; top: 422px; width: 558px; height: 418px; background: linear-gradient(135deg, #b0906f, #8e6e52); }
  .stage-tag { position: absolute; left: 0; top: 0; width: 200px; height: 200px; }
  .stage-tag text {
    font-family: "Open Sans", Arial, sans-serif; font-size: 26px; fill: var(--ink);
    letter-spacing: 1px;
  }

  .divider { position: absolute; left: 34px; top: 1350px; width: 1128px; height: 76px; }

  .content {
    position: absolute; left: 137px; top: 1470px; width: 1020px;
    font-family: "Open Sans", Arial, sans-serif; color: var(--text);
  }
  .headline {
    font-weight: 700; font-size: 58px; line-height: 76px; color: var(--orange);
    margin-bottom: 28px;
  }
  .content p { font-size: 31px; line-height: 40px; margin-bottom: 56px; max-width: 950px; }
  .content p.tight { margin-bottom: 22px; }
  .content p.wide { max-width: 1020px; margin-bottom: 56px; }
  .risk-list { list-style: none; margin-bottom: 30px; width: 920px; }
  .risk-list li { position: relative; padding-left: 39px; font-size: 31px; line-height: 40px; margin-bottom: 38px; }
  .risk-list li:last-child { margin-bottom: 0; }
  .risk-list li::before {
    content: ""; position: absolute; left: 2px; top: 16px; width: 14px; height: 14px;
    border-radius: 50%; background: var(--orange);
  }
  .risk-list strong { color: var(--orange); font-weight: 600; }

  .footer-band {
    position: absolute; left: 34px; top: 2479px; width: 1128px; height: 90px; background: var(--ink);
  }
</style>
</head>
<body>
<main class="flyer">
  <header class="masthead">
    <div class="brand-mark"></div>
    <div class="brand-name">Mesa Ridge Roofing</div>
    <div class="tagline">Polyurethane Sealant</div>
  </header>
  <div class="phone-bar">(555) 014-2271</div>

  <section class="photo-grid">
    <div class="photo photo--tl" role="img" aria-label="Before: cracked, crumbling underlayment beneath roof tiles">
      <svg class="stage-tag" viewBox="0 0 200 200"><polygon points="0,0 200,0 0,200" fill="#e8591e"/><text x="0" y="0" transform="translate(52,112) rotate(-45)">BEFORE</text></svg>
    </div>
    <div class="photo photo--tr" role="img" aria-label="Before: deteriorated underlayment turned to debris">
      <svg class="stage-tag" viewBox="0 0 200 200"><polygon points="0,0 200,0 0,200" fill="#e8591e"/><text x="0" y="0" transform="translate(52,112) rotate(-45)">BEFORE</text></svg>
    </div>
    <div class="photo photo--bl" role="img" aria-label="During: new underlayment being installed with tiles staged on the roof">
      <svg class="stage-tag" viewBox="0 0 200 200"><polygon points="0,0 200,0 0,200" fill="#e8591e"/><text x="0" y="0" transform="translate(50,114) rotate(-45)">DURING</text></svg>
    </div>
    <div class="photo photo--br" role="img" aria-label="After: finished tile roof with vents reinstalled">
      <svg class="stage-tag" viewBox="0 0 200 200"><polygon points="0,0 200,0 0,200" fill="#e8591e"/><text x="0" y="0" transform="translate(60,106) rotate(-45)">AFTER</text></svg>
    </div>
  </section>

  <svg class="divider" viewBox="0 0 1128 76" preserveAspectRatio="none">
    <rect x="0" y="0" width="1128" height="40" fill="#e8591e"/>
    <path d="M0 40 H1128 V68 L1080 72 L1020 66 L900 73 L760 67 L600 74 L420 68 L260 73 L120 67 L0 72 Z" fill="#231f20"/>
  </svg>

  <article class="content">
    <h1 class="headline">The Hidden Clock Ticking<br>Under Your Tiles</h1>
    <p>When a tile roof is installed, the tiles themselves are not water-&#8203;proof—they are simply a shield. The actual waterproofing is done by the felt or synthetic underlayment installed beneath them.</p>
    <p class="tight">In homes of your vintage, this underlayment is now:</p>
    <ul class="risk-list">
      <li><strong>Brittle and Chalky</strong>: It cracks and turns into powder under the constant heat cycles, losing its waterproofing integrity.</li>
      <li><strong>Compromised</strong>: Even a single leak in a neighboring home means the moisture risk has increased exponentially across the entire block.</li>
    </ul>
    <p class="wide">Based on the age and materials used in this specific neighborhood, underlayment failure is not a matter of if, but when.</p>
    <p>Waiting for a visible ceiling stain often means the damage has already spread to the roof deck, rafters, and interior walls. A slow leak can silently cost thousands in remediation before you ever see a drop.</p>
  </article>

  <div class="footer-band"></div>
</main>
</body>
</html>
```